Medspa business needs a webpage

we need a website for a new Medspa company based in Lynden, WA called Lumara Vale Medical Aesthetics. We offer non surgical, cosmetic procedures as well as medical weight loss. We would like a sleek design, with rich colors (dark, emerald green and gold). The website should list our services, pricing and links to book appointments.

```html
<!DOCTYPE html>
<html lang="en">
<head>
<meta charset="UTF-8">
<title>Lumara Vale Medical Aesthetics</title>
<link href="https://fonts.googleapis.com/css2?family=Italiana&family=Poppins:wght@300;400;500&display=swap" rel="stylesheet">
<style>
  :root {
    --bg: #0a1e03;
    --gold: #c29a48;
    --white: #ffffff;
    --text-soft: #e9ece6;
    --photo-a: #6b4a2a;
    --photo-b: #b98558;
    --photo-c: #d9d2c8;
  }
  * { margin: 0; padding: 0; box-sizing: border-box; }
  html, body { width: 1200px; height: 794px; overflow: hidden; }
  body {
    background: var(--bg);
    font-family: "Poppins", sans-serif;
    color: var(--white);
    position: relative;
  }
  .top-rule { position: absolute; left: 76px; top: 0; width: 1124px; height: 1px; background: rgba(255,255,255,0.35); }

  .site-nav { position: absolute; top: 18px; left: 197px; font-size: 8.5px; font-weight: 400; }
  .site-nav a { color: var(--white); text-decoration: none; position: absolute; white-space: nowrap; }
  .site-nav a.is-active { color: var(--gold); }
  .nav-caret { display: inline-block; width: 6px; height: 4px; margin-left: 4px; vertical-align: middle; }

  .brand-name {
    position: absolute; top: 17px; left: 0; width: 1200px; text-align: center;
    font-size: 11px; font-weight: 400; letter-spacing: 1.5px; color: var(--gold);
  }

  .btn-outline {
    position: absolute; border: 1px solid var(--gold); border-radius: 14px;
    color: var(--white); font-size: 7px; font-weight: 400; letter-spacing: 0.5px; text-transform: uppercase;
    display: flex; align-items: center; justify-content: center; text-decoration: none;
  }
  .btn-appointment { left: 914px; top: 13px; width: 92px; height: 24px; }

  .hero { position: absolute; top: 0; left: 0; width: 1200px; text-align: center; }
  .hero-eyebrow { position: absolute; top: 102px; width: 1200px; font-size: 10px; font-weight: 500; color: var(--gold); }
  .hero-title { position: absolute; top: 128px; width: 1200px; font-weight: 300; }
  .hero-title .line-sans { display: block; font-size: 40px; line-height: 56px; }
  .hero-title .line-serif { display: block; font-family: "Italiana", serif; font-size: 42px; line-height: 52px; }
  .hero-copy { position: absolute; top: 247px; left: 452px; width: 296px; font-size: 9px; line-height: 16.5px; color: var(--text-soft); font-weight: 300; }

  .btn-start { left: 509px; top: 302px; width: 89px; height: 24px; }
  .hero-phone {
    position: absolute; left: 610px; top: 307px; font-size: 7.5px; font-weight: 300; color: var(--white);
    border-bottom: 1px solid rgba(194,154,72,0.6); padding-bottom: 2px; display: flex; align-items: center; gap: 6px;
  }

  .hero-photo {
    position: absolute; left: 194px; top: 389px; width: 802px; height: 336px;
    background: linear-gradient(100deg, var(--photo-a) 0%, #3b2a1a 25%, var(--photo-b) 50%, #8b5d3a 62%, var(--photo-c) 80%, #efeae4 100%);
  }
</style>
</head>
<body>
  <div class="top-rule"></div>

  <nav class="site-nav">
    <a class="is-active" href="#" style="left:0">Home</a>
    <a href="#" style="left:57px">About</a>
    <a href="#" style="left:112px">Services</a>
    <a href="#" style="left:176px">Pages<svg class="nav-caret" viewBox="0 0 6 4"><path d="M0.5 0.5 L3 3 L5.5 0.5" fill="none" stroke="#fff" stroke-width="0.8"/></svg></a>
    <a href="#" style="left:245px">Contact</a>
  </nav>

  <div class="brand-name">Lumara Vale</div>

  <a class="btn-outline btn-appointment" href="#">Appointment</a>

  <section class="hero">
    <p class="hero-eyebrow">Reveal Your Natural Beauty</p>
    <h1 class="hero-title">
      <span class="line-sans">Unleash Your Skin's</span>
      <span class="line-serif">True Potential</span>
    </h1>
    <p class="hero-copy">Lorem ipsum dolor sit amet, consectetur adipiscing elit. Ut elit<br>tellus, luctus nec ullamcorper dapibus leo.</p>
    <a class="btn-outline btn-start" href="#">Get Started</a>
    <span class="hero-phone">
      <svg width="8" height="8" viewBox="0 0 24 24" aria-hidden="true"><path d="M5 3h4l2 5-2.5 1.5a11 11 0 0 0 6 6L16 13l5 2v4a2 2 0 0 1-2 2A16 16 0 0 1 3 5a2 2 0 0 1 2-2z" fill="none" stroke="#fff" stroke-width="1.6"/></svg>
      +1 (360) 555 0142
    </span>
  </section>

  <div class="hero-photo" role="img" aria-label="Photo of a client relaxing during a facial mask treatment applied with a brush"></div>
</body>
</html>
```